Cool modern, tech Business card design

Looking for a new business card design for our Managed IT Services company. We would like 2 sides, with the logo one one side horizontally and then the information on the back in either vertical or horizontal. We want our colors from the logo incorporated but also would like to see the color gray in there as well.

Target Market(s)

IT, Information Technology, Tech, Service

Industry/Entity Type

It Service

Contact Information for Business Card

Carl Penner
Managing Partner
(P)555-271-4830 ext xxx
(F)555-271-4831
www.brixtelcore.com

Font styles to use
Sans Serif

Colors
959595
000000
ec1f27

Requirements
Must have
• Logo on one side with some nice design or pattern
• Information on back in either vertical or horizontal format
Nice to have
• For it to look cool, tech, modern, stand out.

```html
<!DOCTYPE html>
<html lang="en">
<head>
<meta charset="utf-8">
<title>Brixtelcore Business Card</title>
<link rel="stylesheet" href="https://fonts.googleapis.com/css2?family=Poppins:wght@500;600&family=Questrial&display=swap">
<style>
  :root {
    --red: #c8142c;
    --black: #231f20;
    --gray: #b3b3b3;
    --white: #ffffff;
    --backdrop: #e2e2e2;
    --text-dark: #222222;
  }
  * { margin: 0; padding: 0; box-sizing: border-box; }
  html, body {
    width: 1125px;
    height: 1200px;
    overflow: hidden;
    background: var(--backdrop);
  }
  .sheet {
    position: relative;
    width: 1125px;
    height: 1200px;
  }
  .card {
    position: absolute;
    left: 171px;
    width: 826px;
    height: 470px;
    border-radius: 26px;
    overflow: hidden;
  }
  .card--front { top: 106px; background: var(--white); }
  .card--back { top: 639px; background: var(--black); }

  .holder { position: absolute; left: 57px; top: 78px; }
  .holder__name {
    font-family: "Poppins", sans-serif;
    font-weight: 600;
    font-size: 31px;
    line-height: 1;
    color: var(--red);
  }
  .holder__title {
    margin-top: 4px;
    font-family: "Questrial", sans-serif;
    font-size: 21px;
    color: var(--text-dark);
  }

  .wordmark {
    font-family: "Poppins", sans-serif;
    font-weight: 500;
    letter-spacing: -0.5px;
    line-height: 1;
  }
  .wordmark--front {
    position: absolute;
    right: 65px;
    top: 84px;
    font-size: 44px;
    color: var(--black);
  }

  .band {
    position: absolute;
    left: 0;
    top: 252px;
    width: 100%;
    height: 154px;
    background: linear-gradient(to right, var(--red) 0, var(--red) 79%, var(--gray) 79%);
  }
  .contact {
    position: absolute;
    left: 58px;
    top: 37px;
    list-style: none;
    font-family: "Questrial", sans-serif;
    font-size: 20px;
    color: var(--white);
  }
  .contact li {
    display: flex;
    align-items: center;
    height: 26px;
  }
  .contact svg { width: 20px; height: 20px; margin-right: 10px; fill: var(--white); }

  .brand-lockup {
    position: absolute;
    left: 0;
    right: 0;
    top: 250px;
    display: flex;
    justify-content: center;
    align-items: center;
    gap: 16px;
  }
  .brand-lockup__mark {
    width: 30px;
    height: 30px;
    border-radius: 6px;
    background: var(--red);
  }
  .wordmark--back { font-size: 56px; color: var(--white); }

  .back-url {
    position: absolute;
    left: 0;
    right: 0;
    top: 396px;
    text-align: center;
    font-family: "Questrial", sans-serif;
    font-size: 20px;
    letter-spacing: 0.45em;
    color: var(--white);
  }
</style>
</head>
<body>
<main class="sheet">
  <section class="card card--front">
    <div class="holder">
      <h1 class="holder__name">Carl Penner</h1>
      <p class="holder__title">Managing Partner</p>
    </div>
    <div class="wordmark wordmark--front">brixtelcore</div>
    <div class="band">
      <ul class="contact">
        <li>
          <svg viewBox="0 0 24 24" aria-hidden="true"><path d="M6.6 10.8a15 15 0 0 0 6.6 6.6l2.2-2.2a1 1 0 0 1 1-.25 11.4 11.4 0 0 0 3.6.57 1 1 0 0 1 1 1V20a1 1 0 0 1-1 1A17 17 0 0 1 3 4a1 1 0 0 1 1-1h3.5a1 1 0 0 1 1 1c0 1.25.2 2.45.57 3.6a1 1 0 0 1-.25 1z"/></svg>
          555-271-4830 ext xxx
        </li>
        <li>
          <svg viewBox="0 0 24 24" aria-hidden="true"><path d="M7 3h8l3 3v4H7z M3 11h18v8h-3v-3H6v3H3z M7 17h10v4H7z"/></svg>
          555-271-4831
        </li>
        <li>
          <svg viewBox="0 0 24 24" aria-hidden="true"><path d="M12 2a10 10 0 1 0 0 20 10 10 0 0 0 0-20zm-1 17.9A8 8 0 0 1 4.2 10L9 14.8V16a2 2 0 0 0 2 2zm6.9-2.5A2 2 0 0 0 16 16h-1v-3a1 1 0 0 0-1-1H8v-2h2a1 1 0 0 0 1-1V7h2a2 2 0 0 0 2-2v-.4a8 8 0 0 1 2.9 12.8z"/></svg>
          www.brixtelcore.com
        </li>
      </ul>
    </div>
  </section>

  <section class="card card--back">
    <div class="brand-lockup">
      <div class="wordmark wordmark--back">brixtelcore</div>
      <span class="brand-lockup__mark" aria-hidden="true"></span>
    </div>
    <p class="back-url">www.brixtelcore.com</p>
  </section>
</main>
</body>
</html>
```